Velnora Engineering Consulting

We need a website design for a new company based in South Africa called Brundel Consulting, it is a formidable engineering and consulting company with a background in Electrical and Mechanical design.We adopt a problem-solving methodology which allows us to present our clients with quick and flexible results. We offer complete engineering solutions from consulting, engineering design and even supply of equipment.
Target Market(s)
Government, private sector and public sector
Industry/Entity Type
Engineering Consulting
Number of Pages Required
5+ page
Colors
Designer to choose colors to be used in the design.
Requirements
Must have
- Must match the design of the profile, must enhance the profile look
Nice to have
- lates in terms of website design
Should not have
- Should be clean as the profile, should not deviate from the feel of the profile

```html
<!DOCTYPE html>
<html lang="en">
<head>
<meta charset="utf-8">
<title>Brundel Consulting</title>
<link href="https://fonts.googleapis.com/css2?family=Montserrat:wght@400;500;600;700&display=swap" rel="stylesheet">
<style>
:root{
  --navy:#1e2a3a;
  --navy-deep:#172230;
  --ink:#222a35;
  --text:#555b63;
  --muted:#8a9099;
  --light:#f4f4f4;
  --line:#d9dcdf;
  --white:#ffffff;
  --card:#3f4a57;
}
*{box-sizing:border-box;margin:0;padding:0}
html,body{width:1200px;height:3186px;overflow:hidden}
body{font-family:"Montserrat",Arial,sans-serif;color:var(--text);background:var(--white);position:relative}
section,header,footer{position:absolute;left:0;width:1200px}
.abs{position:absolute}
svg{display:block}

/* hero */
.hero{top:0;height:599px;overflow:hidden}
.hero-photo{position:absolute;inset:0;background:linear-gradient(180deg,#1a2434 0%,#2b3c58 30%,#6d6f80 48%,#c98a5a 55%,#3a4560 66%,#1a2236 100%)}
.topbar{position:absolute;top:0;left:0;width:1200px;height:30px}
.topbar .contact{position:absolute;top:8px;font-size:11px;color:var(--white);display:flex;align-items:center;gap:7px}
.brand{position:absolute;left:149px;top:18px;font-size:26px;font-weight:500;color:var(--white);letter-spacing:1px}
.nav{position:absolute;top:62px;right:180px;display:flex;gap:18px;align-items:center;font-size:11.5px;font-weight:600;color:var(--white)}
.slide-arrow{position:absolute;top:284px;width:32px;height:32px;border-radius:50%;background:rgba(255,255,255,.55)}
.mouse{position:absolute;left:589px;top:537px;width:22px;height:38px;border:2px solid rgba(255,255,255,.8);border-radius:11px}
.mouse::after{content:"";position:absolute;left:8px;top:7px;width:2px;height:8px;background:rgba(255,255,255,.8)}

/* about */
.about{top:599px;height:435px;background:var(--light)}
.about-mark{left:149px;top:80px;font-size:52px;font-weight:400;color:#b4b8bd;letter-spacing:1px}
.about h2{left:378px;top:72px;font-size:24px;font-weight:600;color:var(--ink)}
.about .copy{left:378px;top:105px;width:672px;font-size:13px;line-height:21px}
.about .copy p+p{margin-top:17px}
.pillar{top:280px;width:400px}
.pillar h3{position:absolute;left:75px;top:3px;font-size:16px;font-weight:700;color:var(--ink)}
.pillar p{position:absolute;left:75px;top:31px;width:330px;font-size:11.5px;line-height:20px;text-align:justify}

h2.section-title{position:absolute;left:0;width:1200px;text-align:center;font-size:24px;font-weight:600;letter-spacing:.5px}
.lede{position:absolute;left:250px;width:700px;text-align:center;font-size:13px;line-height:21px}

/* products */
.products{top:1034px;height:542px}
.products h2{top:60px;color:var(--ink)}
.products .lede{top:100px}
.service{top:196px;width:302px;height:272px;text-align:center}
.service.active{background:var(--card);box-shadow:0 3px 8px rgba(0,0,0,.25);color:#d8dde3}
.service .icon{margin:20px auto 0;width:94px;height:94px;border-radius:50%;background:var(--white);border:3px solid var(--ink);display:flex;align-items:center;justify-content:center}
.service h3{margin-top:22px;font-size:17px;font-weight:600;color:var(--ink);letter-spacing:.3px}
.service.active h3{color:var(--white)}
.service p{margin:12px auto 0;width:240px;font-size:13px;line-height:24px}
.carousel-btn{position:absolute;top:320px;width:26px;height:26px;border-radius:50%;background:#b8bcc1}

/* consulting */
.consulting{top:1576px;height:544px;background:var(--navy);color:var(--white)}
.consulting-photo{position:absolute;inset:0;background:radial-gradient(ellipse at 75% 30%,rgba(90,110,135,.45),transparent 60%),radial-gradient(ellipse at 20% 70%,rgba(60,80,105,.35),transparent 55%)}
.consulting h2{top:58px;color:var(--white)}
.consulting .lede{top:110px;color:#dfe4ea}
.col{top:226px;width:300px}
.col .icon{width:76px;height:76px;border-radius:50%;border:3px solid var(--white);background:var(--navy-deep);display:flex;align-items:center;justify-content:center}
.col h3{margin-top:21px;font-size:17px;font-weight:600}
.col ul{list-style:none;margin-top:8px;font-size:13px;line-height:22.5px;color:#e6eaef}
.col li::before{content:"› ";font-weight:700}

/* industries */
.industries{top:2120px;height:372px;background:var(--light)}
.industries h2{top:73px;color:var(--ink)}
.industry{top:156px;width:200px;text-align:center}
.industry .icon{margin:0 auto;width:94px;height:94px;border-radius:50%;border:3px solid var(--ink);background:var(--white);display:flex;align-items:center;justify-content:center}
.industry.active .icon{background:var(--ink)}
.industry h3{margin-top:16px;font-size:18px;font-weight:600;color:var(--ink)}
.divider{top:140px;width:1px;height:165px;background:var(--line)}

/* contact */
.contact{top:2492px;height:541px}
.contact h2{top:75px;color:var(--ink)}
.contact .sub{position:absolute;top:115px;width:1200px;text-align:center;font-size:13px;letter-spacing:1.5px;color:var(--muted)}
.field{position:absolute;border:1px solid #e3e5e8;background:var(--white);font-size:10px;color:#a8adb3;padding:8px 10px}
.send{position:absolute;left:389px;top:441px;width:124px;height:28px;border-radius:14px;background:var(--ink);color:var(--white);font-size:11px;font-weight:700;display:flex;align-items:center;justify-content:center;letter-spacing:.5px}
.map{position:absolute;left:616px;top:163px;width:435px;height:276px;background:radial-gradient(ellipse at center,#c9ccd0 0%,#e4e6e8 60%,#ffffff 100%);border-radius:6px}
.address{position:absolute;left:616px;top:439px;width:433px;height:27px;background:var(--white);box-shadow:0 1px 5px rgba(0,0,0,.2);font-size:11px;color:var(--ink);display:flex;align-items:center;gap:10px;padding-left:14px}

/* footer */
.site-footer{top:3033px;height:153px;background:var(--ink)}
.to-top{position:absolute;left:582px;top:-19px;width:38px;height:38px;border-radius:50%;background:var(--white);box-shadow:0 1px 4px rgba(0,0,0,.3);display:flex;align-items:center;justify-content:center}
.badge{position:absolute;left:149px;top:42px;width:170px;height:48px;border-radius:4px;background:#d7dbe0}
.footer-links{position:absolute;right:151px;top:77px;font-size:11px;color:var(--white);text-align:right;line-height:19px}
.footer-links strong{font-weight:600}
</style>
</head>
<body>

<header class="hero">
  <div class="hero-photo" role="img" aria-label="Night city skyline at dusk with glowing technology icons over the towers"></div>
  <div class="topbar">
    <div class="contact" style="left:757px">
      <svg width="12" height="12" viewBox="0 0 24 24"><path fill="#fff" d="M6.6 10.8a15 15 0 0 0 6.6 6.6l2.2-2.2a1 1 0 0 1 1-.25 11.4 11.4 0 0 0 3.6.57 1 1 0 0 1 1 1V20a1 1 0 0 1-1 1A17 17 0 0 1 3 4a1 1 0 0 1 1-1h3.5a1 1 0 0 1 1 1c0 1.25.2 2.45.57 3.57a1 1 0 0 1-.25 1z"/></svg>
      +27 (0) 11 555 0142
    </div>
    <div class="contact" style="left:903px">
      <svg width="14" height="10" viewBox="0 0 24 16"><rect x="1" y="1" width="22" height="14" fill="none" stroke="#fff" stroke-width="2"/><path d="M1 1l11 8 11-8" fill="none" stroke="#fff" stroke-width="2"/></svg>
      info@brundelcs.com
    </div>
  </div>
  <div class="brand">Brundel</div>
  <nav class="nav">
    <svg width="14" height="13" viewBox="0 0 24 22"><path fill="#fff" d="M12 1 1 11h3v10h6v-6h4v6h6V11h3z"/></svg>
    <span>ABOUT</span><span>PRODUCTS &amp; SERVICES</span><span>INDUSTRIES WE SERVE</span><span>CONTACT US</span><span>CLIENTS</span>
  </nav>
  <div class="slide-arrow" style="left:36px"><svg width="32" height="32" viewBox="0 0 32 32"><path d="M18 10l-6 6 6 6" fill="none" stroke="#1e2a3a" stroke-width="3"/></svg></div>
  <div class="slide-arrow" style="left:1131px"><svg width="32" height="32" viewBox="0 0 32 32"><path d="M14 10l6 6-6 6" fill="none" stroke="#1e2a3a" stroke-width="3"/></svg></div>
  <div class="mouse"></div>
</header>

<section class="about">
  <div class="abs about-mark">Brundel</div>
  <h2 class="abs">ABOUT US</h2>
  <div class="abs copy">
    <p>Established in 2014, Brundel Consulting is a formidable engineering and consulting company with a background in Electrical and Mechanical design. We adopt a problem-solving methodology which allows us to present our clients with quick and flexible results. We offer complete engineering</p>
    <p>With over 15 years combined experience in Engineering and Electrical Technology, we create solutions of the highest innovative standard. solutions from consulting, engineering design and even supply of equipment.</p>
  </div>
  <div class="abs pillar" style="left:149px">
    <svg width="62" height="40" viewBox="0 0 62 40"><path d="M3 20C12 8 24 4 31 4s19 4 28 16C50 32 38 36 31 36S12 32 3 20z" fill="none" stroke="#9aa0a7" stroke-width="3"/><circle cx="31" cy="20" r="9" fill="none" stroke="#9aa0a7" stroke-width="3"/><circle cx="31" cy="20" r="3" fill="#9aa0a7"/></svg>
    <h3>OUR VISION</h3>
    <p>We aim to become the preferred engineering design and consulting firm within the South African Engineering industry for prominent companies in the market.</p>
  </div>
  <div class="abs pillar" style="left:629px">
    <svg width="52" height="44" viewBox="0 0 52 44"><circle cx="30" cy="22" r="19" fill="none" stroke="#9aa0a7" stroke-width="3"/><circle cx="30" cy="22" r="11" fill="none" stroke="#9aa0a7" stroke-width="3"/><circle cx="30" cy="22" r="4" fill="#9aa0a7"/><path d="M2 8l28 14" stroke="#9aa0a7" stroke-width="3"/></svg>
    <h3>OUR MISSION</h3>
    <p>We offer our clients technologically innovative service, allowing us to create high levels of customer satisfaction.</p>
  </div>
</section>

<section class="products">
  <h2 class="section-title">PRODUCTS &amp; SERVICES</h2>
  <p class="lede">Using innovation and technology, we provide a range of Mechanical and Electrical design, electrification, equipment supply, Mechanical and Electrical products for mining houses, process plants, government departments, municipalities, state-owned entities and rail companies.</p>
  <div class="carousel-btn" style="left:104px"><svg width="26" height="26" viewBox="0 0 26 26"><path d="M15 8l-5 5 5 5" fill="none" stroke="#fff" stroke-width="2.5"/></svg></div>
  <div class="carousel-btn" style="left:1066px"><svg width="26" height="26" viewBox="0 0 26 26"><path d="M11 8l5 5-5 5" fill="none" stroke="#fff" stroke-width="2.5"/></svg></div>
  <div class="abs service" style="left:161px">
    <div class="icon"><svg width="44" height="44" viewBox="0 0 24 24"><path fill="#222a35" d="M22.7 19 13.6 9.9c.9-2.3.4-5-1.5-6.9-2-2-5-2.4-7.4-1.3L9 6 6 9 1.6 4.7C.4 7.1.9 10.1 2.9 12.1c1.9 1.9 4.6 2.4 6.9 1.5l9.1 9.1c.4.4 1 .4 1.4 0l2.3-2.3c.5-.4.5-1.1.1-1.4z"/></svg></div>
    <h3>ENGINEERING &amp; INSTALLATION</h3>
    <p>We take your company's wish list and assess how much power is required to run your building.</p>
  </div>
  <div class="abs service active" style="left:457px">
    <div class="icon"><svg width="44" height="44" viewBox="0 0 24 24"><circle cx="12" cy="12" r="9" fill="none" stroke="#3f4a57" stroke-width="2.5" stroke-dasharray="3 2"/><circle cx="12" cy="12" r="4" fill="#3f4a57"/></svg></div>
    <h3>ELECTRICAL DESIGN</h3>
    <p>We take your company's wish list and assess how much power is required to run your building.</p>
  </div>
  <div class="abs service" style="left:760px">
    <div class="icon"><svg width="44" height="44" viewBox="0 0 24 24"><circle cx="9" cy="14" r="5" fill="none" stroke="#222a35" stroke-width="3" stroke-dasharray="2.5 1.5"/><circle cx="17" cy="7" r="3.5" fill="none" stroke="#222a35" stroke-width="2.5" stroke-dasharray="2 1.3"/><path d="M15 14l-2 4h3l-2 4" stroke="#222a35" stroke-width="1.5" fill="none"/></svg></div>
    <h3>TURNKEY ELECTRIFICATION</h3>
    <p>It is progressively becoming standard for new developments in Southern Africa to be electrically powered.</p>
  </div>
</section>

<section class="consulting">
  <div class="consulting-photo" role="img" aria-label="Faded photo of engineers reviewing plans, overlaid with line icons"></div>
  <h2 class="section-title">CONSULTING SERVICES</h2>
  <p class="lede">Using innovation and technology, we provide a range of Mechanical and Electrical design, electrification, equipment supply, Mechanical and Electrical products for mining houses, process plants, government departments, municipalities, state-owned entities and rail companies.</p>
  <div class="abs col" style="left:153px">
    <div class="icon"><svg width="36" height="40" viewBox="0 0 36 40"><circle cx="18" cy="12" r="8" fill="#fff"/><path d="M3 38c0-9 7-15 15-15s15 6 15 15z" fill="#fff"/></svg></div>
    <h3>Technical Advice</h3>
    <ul><li>Writing Mine Code of practice (COP)</li><li>Equipment trade-off</li><li>Practicality Assurance</li><li>Equipment Assessment</li><li>Reporting</li></ul>
  </div>
  <div class="abs col" style="left:486px">
    <div class="icon"><svg width="40" height="36" viewBox="0 0 40 36"><rect x="3" y="3" width="34" height="20" rx="10" fill="#fff"/><circle cx="12" cy="13" r="2.5" fill="#172230"/><circle cx="20" cy="13" r="2.5" fill="#172230"/><circle cx="28" cy="13" r="2.5" fill="#172230"/><path d="M12 23h16l-8 10z" fill="#fff"/></svg></div>
    <h3>Design Reviews</h3>
    <ul><li>Calculation Validations</li><li>Equipment Sizing</li><li>Design Practicality Assessment</li></ul>
  </div>
  <div class="abs col" style="left:786px">
    <div class="icon"><svg width="40" height="40" viewBox="0 0 40 40"><circle cx="13" cy="13" r="7" fill="none" stroke="#fff" stroke-width="2.5"/><circle cx="27" cy="27" r="7" fill="none" stroke="#fff" stroke-width="2.5"/><circle cx="28" cy="11" r="4" fill="none" stroke="#fff" stroke-width="2.5"/><path d="M18 18l4 4" stroke="#fff" stroke-width="2.5"/></svg></div>
    <h3>Execution</h3>
    <ul><li>Owner's Engineer Onsite Supervision</li><li>Operational Assistance</li></ul>
  </div>
</section>

<section class="industries">
  <h2 class="section-title">INDUSTRIES WE SERVE</h2>
  <div class="abs industry" style="left:168px">
    <div class="icon"><svg width="48" height="44" viewBox="0 0 48 44"><path d="M4 40 20 12l8 12 5-6 11 22z" fill="#9aa0a7"/><path d="M14 16l12-8M20 4l6 4" stroke="#222a35" stroke-width="3"/></svg></div>
    <h3>Mining</h3>
  </div>
  <div class="abs divider" style="left:373px"></div>
  <div class="abs industry active" style="left:391px">
    <div class="icon"><svg width="48" height="48" viewBox="0 0 48 48"><path d="M10 38 34 14M38 38 14 14" stroke="#fff" stroke-width="5"/><rect x="28" y="6" width="14" height="8" fill="#fff" transform="rotate(45 35 10)"/><circle cx="12" cy="12" r="6" fill="#fff"/></svg></div>
    <h3>Construction</h3>
  </div>
  <div class="abs divider" style="left:599px"></div>
  <div class="abs industry" style="left:612px">
    <div class="icon"><svg width="48" height="44" viewBox="0 0 48 44"><path d="M24 3 4 13h40z" fill="#222a35"/><rect x="8" y="16" width="5" height="18" fill="#222a35"/><rect x="17" y="16" width="5" height="18" fill="#222a35"/><rect x="26" y="16" width="5" height="18" fill="#222a35"/><rect x="35" y="16" width="5" height="18" fill="#222a35"/><rect x="4" y="36" width="40" height="5" fill="#222a35"/></svg></div>
    <h3>Public Sector</h3>
  </div>
  <div class="abs divider" style="left:822px"></div>
  <div class="abs industry" style="left:832px">
    <div class="icon"><svg width="48" height="48" viewBox="0 0 48 48"><circle cx="24" cy="24" r="14" fill="none" stroke="#9aa0a7" stroke-width="10" stroke-dasharray="7 4"/><circle cx="24" cy="24" r="6" fill="#9aa0a7"/></svg></div>
    <h3>EPCMs</h3>
  </div>
</section>

<section class="contact">
  <h2 class="section-title">CONTACT US</h2>
  <p class="sub">Please don't Hesitate to Contact Us.</p>
  <div class="field" style="left:149px;top:188px;width:174px;height:28px">Your Name</div>
  <div class="field" style="left:336px;top:188px;width:174px;height:28px">Your Email</div>
  <div class="field" style="left:149px;top:229px;width:361px;height:200px">Write a Message</div>
  <div class="send">SEND MESSAGE</div>
  <div class="map" role="img" aria-label="Grey world map with location pins"></div>
  <div class="address">
    <svg width="10" height="14" viewBox="0 0 10 14"><path d="M5 0a5 5 0 0 0-5 5c0 4 5 9 5 9s5-5 5-9a5 5 0 0 0-5-5zm0 7a2 2 0 1 1 0-4 2 2 0 0 1 0 4z" fill="#222a35"/></svg>
    14 Acacia Lane, Rivonia, Sandton, 2128, South Africa
  </div>
</section>

<footer class="site-footer">
  <div class="to-top"><svg width="16" height="16" viewBox="0 0 16 16"><path d="M3 11l5-5 5 5" fill="none" stroke="#222a35" stroke-width="2.5"/></svg></div>
  <div class="badge"></div>
  <div class="footer-links">
    About &nbsp;|&nbsp; Contact &nbsp;|&nbsp; Terms &amp; Conditions &nbsp;|&nbsp; Privacy Policy<br>
    <strong>Copyright © 2019, Brundel Consulting, All Rights reserved.</strong>
  </div>
</footer>

</body>
</html>
```